Business card design needed

I need a business card for my Sydney Painting Business, that specialises in painting High -end residential homes. i want the design to look clean, modern and edgy. i also want a logo next to the RL Decorating, using RLD together.

Industry/Entity Type

Residential

Contact Information for Business Card

RL Decorating (business name),LIC 871536K, Rob Lindqvist, robert.lindqvist@brushmail.example, mobile 0419352807

```html
<!DOCTYPE html>
<html lang="en">
<head>
<meta charset="utf-8">
<title>RL Decorating — Business Card</title>
<link rel="stylesheet" href="https://fonts.googleapis.com/css2?family=Bebas+Neue&display=swap">
<style>
  :root {
    --card-light: #e2ebe7;
    --card-mid: #d8e3df;
    --card-edge: #c9d3d1;
    --ink: #141414;
    --hand-red: #d10d14;
    --hand-black: #151515;
    --hand-blue: #48b7e4;
  }
  html, body {
    margin: 0;
    padding: 0;
    width: 1200px;
    height: 741px;
    overflow: hidden;
  }
  .card {
    position: relative;
    width: 1200px;
    height: 741px;
    overflow: hidden;
    background: radial-gradient(ellipse at 40% 35%, var(--card-light) 0%, var(--card-mid) 60%, var(--card-edge) 100%);
    font-family: "Bebas Neue", "Arial Narrow", sans-serif;
    color: var(--ink);
  }
  .hands-art {
    position: absolute;
    left: 643px;
    top: 32px;
    width: 440px;
    height: 510px;
  }
  .business-name {
    position: absolute;
    left: 66px;
    top: 296px;
    margin: 0;
    font-size: 142px;
    line-height: 1;
    font-weight: 400;
    letter-spacing: 1px;
    white-space: nowrap;
    text-shadow: 0 14px 14px rgba(0, 0, 0, 0.12);
  }
  .contact-list {
    position: absolute;
    left: 70px;
    top: 452px;
    margin: 0;
    padding: 0;
    list-style: none;
  }
  .contact-list li {
    font-size: 47px;
    line-height: 59.5px;
    white-space: nowrap;
    letter-spacing: 0.5px;
    text-shadow: 0 10px 12px rgba(0, 0, 0, 0.12);
  }
</style>
</head>
<body>
  <main class="card">
    <svg class="hands-art" viewBox="0 0 440 510" role="img" aria-label="Three overlapping painted handprints: a large red hand, a smaller black hand and a small light-blue child's hand">
      <defs>
        <linearGradient id="hands-tones" x1="0" y1="0" x2="1" y2="1">
          <stop offset="0" stop-color="var(--hand-red)"/>
          <stop offset="0.6" stop-color="var(--hand-red)"/>
          <stop offset="0.8" stop-color="var(--hand-black)"/>
          <stop offset="1" stop-color="var(--hand-blue)"/>
        </linearGradient>
      </defs>
      <rect x="0" y="0" width="440" height="510" rx="48" fill="url(#hands-tones)"/>
    </svg>

    <h1 class="business-name">RL Decorating</h1>

    <ul class="contact-list">
      <li class="licence">LIC 871536K</li>
      <li class="owner">Rob Lindqvist</li>
      <li class="email">robert.lindqvist@brushmail.example</li>
      <li class="mobile">Mobile 0419352807</li>
    </ul>
  </main>
</body>
</html>
```